Greatest Mom Greeting Card

A 5in x 7in greeting card design for a company that sells political humor greeting cards online. The specifications are as follows:

Front Text: "You’re the best mom. The greatest mom. The most beautiful mom. VERY SUCCESSFUL." in scripty font for everything but the portion in all caps. All caps type should be in a bold san serif condensed font.

Front Art: Think flowers and light pastels.

Inner Right Text: "Happy Mother’s Day. THE HAPPIEST." same script font for Happy Mother's Day, and same bold san-serif font for The Happiest.

Inner Right Art: Include graphic/illustration of Harold Brennick with thumbs up.

```html
<!DOCTYPE html>
<html lang="en">
<head>
<meta charset="utf-8">
<title>Greatest Mom Greeting Card</title>
<link rel="stylesheet" href="https://fonts.googleapis.com/css2?family=Dancing+Script:wght@500&family=Open+Sans:wght@800&display=swap">
<style>
  :root {
    --backdrop: #cdcecf;
    --card: #ffffff;
    --sky: #9dcdef;
    --wave-deep: #7aa2d8;
    --wave-mid: #73b2e0;
    --wave-light: #bfe3f5;
    --frame: #8ecbee;
    --ink: #222222;
    --petal: #5fc4d8;
    --petal-soft: #bfe8ef;
    --portrait: #3a3f63;
    --portrait-soft: #e8c9a8;
  }
  * { margin: 0; padding: 0; box-sizing: border-box; }
  html, body { width: 1200px; height: 864px; overflow: hidden; }
  body { background: var(--backdrop); position: relative; }

  .card { position: absolute; background: var(--card); overflow: hidden; }
  .card--front { left: 48px; top: 62px; width: 528px; height: 740px; }
  .card--inside { left: 624px; top: 62px; width: 526px; height: 740px; }

  .wave-band { position: absolute; left: 0; top: 0; width: 528px; height: 80px; }

  .message-box {
    position: absolute; left: 55px; top: 161px; width: 419px; height: 349px;
    background: var(--sky);
  }
  .message-box__inner {
    position: absolute; left: 15px; top: 15px; right: 15px; bottom: 15px;
    border: 2px solid var(--card);
    display: flex; flex-direction: column; align-items: center; justify-content: center;
    padding-top: 6px;
  }
  .script {
    font-family: "Dancing Script", cursive; font-weight: 500; color: var(--ink);
    text-align: center;
  }
  .message-box .script { font-size: 33px; line-height: 49px; }
  .headline {
    font-family: "Open Sans", sans-serif; font-weight: 800; color: var(--ink);
    text-align: center; letter-spacing: 0.5px;
  }
  .message-box .headline { font-size: 35px; line-height: 46px; margin-top: 6px; }

  .flower-bed {
    position: absolute; left: 22px; top: 568px; width: 484px; height: 172px;
    background: linear-gradient(180deg, var(--petal-soft), var(--petal));
    border-radius: 60px 60px 0 0;
  }

  .inside-frame {
    position: absolute; left: 20px; top: 24px; width: 486px; height: 694px;
    border: 12px solid var(--frame);
  }
  .greeting { position: absolute; left: 0; top: 142px; width: 526px; }
  .greeting .script { font-size: 44px; line-height: 56px; }
  .greeting .headline { font-size: 44px; line-height: 60px; margin-top: 12px; }

  .portrait {
    position: absolute; left: 154px; top: 334px; width: 270px; height: 242px;
    border-radius: 121px 40px 40px 121px;
    background: linear-gradient(160deg, var(--portrait-soft), var(--portrait));
  }
  .blossom {
    position: absolute; border-radius: 50%;
    background: radial-gradient(circle, var(--petal) 0%, var(--petal-soft) 100%);
  }
  .blossom--a { left: 52px;  top: 556px; width: 86px; height: 86px; }
  .blossom--b { left: 160px; top: 620px; width: 62px; height: 62px; }
  .blossom--c { left: 286px; top: 610px; width: 74px; height: 74px; }
  .blossom--d { left: 394px; top: 586px; width: 62px; height: 62px; }
</style>
</head>
<body>
  <section class="card card--front" aria-label="Card front">
    <svg class="wave-band" viewBox="0 0 528 80" aria-hidden="true">
      <rect width="528" height="80" fill="var(--wave-mid)"/>
      <path d="M0 40 C90 20 150 60 230 62 C320 64 380 30 528 50 L528 0 L0 0 Z" fill="var(--wave-mid)"/>
      <path d="M0 34 C110 18 190 78 290 70 C380 62 440 40 528 58 L528 80 L0 80 Z" fill="var(--card)"/>
      <path d="M0 34 C110 18 190 60 250 66 C330 74 430 44 528 44 L528 60 C440 54 380 70 300 74 C200 80 110 30 0 50 Z" fill="var(--wave-deep)"/>
      <path d="M180 62 C230 54 280 56 330 60 C290 70 230 72 180 62 Z" fill="var(--wave-light)"/>
    </svg>
    <div class="message-box">
      <div class="message-box__inner">
        <p class="script">You’re the best mom.</p>
        <p class="script">The greatest mom.</p>
        <p class="script">The most beautiful mom.</p>
        <p class="headline">VERY SUCCESSFUL.</p>
      </div>
    </div>
    <div class="flower-bed" role="img" aria-label="Row of pastel blue and teal flowers on thin stems"></div>
  </section>

  <section class="card card--inside" aria-label="Card inside right">
    <div class="inside-frame"></div>
    <div class="greeting">
      <p class="script">Happy Mother’s Day.</p>
      <p class="headline">THE HAPPIEST.</p>
    </div>
    <div class="portrait" role="img" aria-label="Cartoon illustration of Harold Brennick in a suit giving a thumbs up inside a blue circle"></div>
    <div class="blossom blossom--a" role="img" aria-label="Pastel blue flower"></div>
    <div class="blossom blossom--b" role="img" aria-label="Pastel blue flower"></div>
    <div class="blossom blossom--c" role="img" aria-label="Pastel blue flower"></div>
    <div class="blossom blossom--d" role="img" aria-label="Pastel blue flower"></div>
  </section>
</body>
</html>
```